6"x6" Ad for stair elevators and lift chairs

We are a small medical company that offers a wide range of medical equipment but we are looking to focus this advertisement on our Varnel Stair Elevators and Caldor lift Chairs. We will Publish a 6" x 6" advertisement. We are leaning toward the theme of "Need a Lift?" Looking to include Image of a Varnel Stair Elevator, Caldor Lift chair, Company name, Phone Number and QR Code to our website. Were open to different. Ad can not be seasonal as we may run it more then once. Looking for eye catching and professional.

```html
<!DOCTYPE html>
<html lang="en">
<head>
<meta charset="utf-8">
<title>Need a Lift? – Kestrel Medical</title>
<link rel="stylesheet" href="https://fonts.googleapis.com/css2?family=Poppins:ital,wght@0,400;0,500;0,600;0,700;1,700&family=Lato:wght@400&display=swap">
<style>
  :root {
    --bg: #1e1f26;
    --blue: #1d6fbd;
    --blue-bright: #1f78cc;
    --steel: #5a88b4;
    --white: #ffffff;
    --photo-stairs-a: #e2cf9f;
    --photo-stairs-b: #6b5a48;
    --photo-chair-a: #ffffff;
    --photo-chair-b: #a18d78;
  }
  * { box-sizing: border-box; margin: 0; padding: 0; }
  html, body { width: 1200px; height: 1200px; overflow: hidden; background: var(--bg); }
  .ad {
    position: relative;
    width: 1200px;
    height: 1200px;
    background: var(--bg);
    font-family: "Poppins", sans-serif;
    color: var(--white);
    overflow: hidden;
  }
  .ad__swoosh { position: absolute; inset: 0; width: 1200px; height: 1200px; }

  .brand {
    position: absolute;
    left: 70px;
    top: 150px;
    width: 270px;
    text-align: center;
  }
  .brand__mark {
    display: block;
    width: 46px;
    height: 46px;
    margin: 0 auto 22px;
    background: var(--blue-bright);
  }
  .brand__name {
    font-family: "Poppins", sans-serif;
    font-weight: 700;
    font-size: 40px;
    line-height: 1.05;
    letter-spacing: 2px;
    color: var(--blue-bright);
    text-transform: uppercase;
  }
  .brand__phone {
    margin-top: 14px;
    font-family: "Poppins", sans-serif;
    font-weight: 700;
    font-style: italic;
    font-size: 33px;
    letter-spacing: 1px;
    color: var(--blue-bright);
  }

  .headline {
    position: absolute;
    left: 62px;
    top: 368px;
    font-weight: 500;
    font-size: 118px;
    line-height: 1.1;
  }
  .headline__top { display: block; color: var(--white); }
  .headline__accent { display: block; color: var(--steel); }

  .tagline {
    position: absolute;
    left: 68px;
    top: 645px;
    width: 500px;
    font-family: "Lato", sans-serif;
    font-size: 31px;
    line-height: 1.45;
    color: var(--white);
  }

  .cta {
    position: absolute;
    left: 0;
    top: 955px;
    width: 600px;
    height: 124px;
    background: var(--blue);
    border-radius: 0 62px 62px 0;
    display: flex;
    align-items: center;
    text-decoration: none;
  }
  .cta__label {
    margin-left: 100px;
    font-weight: 500;
    font-size: 48px;
    letter-spacing: 1px;
    color: var(--white);
  }
  .cta__icon {
    position: absolute;
    right: 12px;
    top: 12px;
    width: 100px;
    height: 100px;
    border-radius: 50%;
    background: var(--bg);
  }

  .website {
    position: absolute;
    left: 100px;
    top: 1104px;
    font-family: "Lato", sans-serif;
    font-size: 31px;
    color: var(--white);
  }

  .product {
    position: absolute;
    left: 650px;
    width: 494px;
    height: 498px;
    border: 11px solid var(--blue-bright);
    border-radius: 64px;
    overflow: hidden;
    background: var(--bg);
  }
  .product--stairs { top: 119px; }
  .product--chair { top: 647px; }
  .product__fill { width: 100%; height: 100%; }
  .product--stairs .product__fill {
    background: linear-gradient(135deg, var(--photo-stairs-a) 0%, #c9b285 45%, var(--photo-stairs-b) 100%);
  }
  .product--chair .product__fill {
    background: radial-gradient(ellipse at 55% 48%, var(--photo-chair-b) 0%, #bfae9b 38%, var(--photo-chair-a) 72%);
  }
</style>
</head>
<body>
<main class="ad">
  <svg class="ad__swoosh" viewBox="0 0 1200 1200" aria-hidden="true">
    <path d="M 870 -20 C 720 120, 660 420, 760 620 C 840 770, 1020 850, 1220 865"
          fill="none" stroke="#1f78cc" stroke-width="28" stroke-linecap="butt"/>
  </svg>

  <header class="brand">
    <span class="brand__mark"></span>
    <p class="brand__name">Kestrel<br>Medical</p>
    <p class="brand__phone">330-555-0148</p>
  </header>

  <h1 class="headline">
    <span class="headline__top">Need a</span>
    <span class="headline__accent">Lift?</span>
  </h1>

  <p class="tagline">Get the best chair experience you will ever have in your life, stay relaxed and work relaxed.</p>

  <a class="cta" href="#">
    <span class="cta__label">ORDER NOW</span>
    <svg class="cta__icon" viewBox="0 0 100 100" aria-hidden="true">
      <circle cx="50" cy="50" r="50" fill="#1e1f26"/>
      <path d="M 28 50 H 70 M 55 34 L 71 50 L 55 66" fill="none" stroke="#ffffff" stroke-width="7" stroke-linecap="round" stroke-linejoin="round"/>
    </svg>
  </a>

  <p class="website">www.kestrelmedical.com</p>

  <figure class="product product--stairs">
    <div class="product__fill" role="img" aria-label="Photo of a smiling woman riding a Varnel Stair Elevator up a carpeted staircase"></div>
  </figure>
  <figure class="product product--chair">
    <div class="product__fill" role="img" aria-label="Photo of a taupe Caldor Lift chair recliner with cup holders, raised on its lift base"></div>
  </figure>
</main>
</body>
</html>
```